New Infographic Design Project

Hi, I have another project to work on if you are interested. It is a horizontal style infographic with 6 steps. It should display the step Number (1-6), Title, and an Icon.

Step 1 - Strong Phone Interview
Step 2 - Pre-Employment
Step 3 - Prep & Do In-Person Interview
Step 4 - Second Interview
Step 5 - Reference Checks
Step 6 - Job Offer

More flexible on colors with this one, but keep it professional.

```html
<!DOCTYPE html>
<html lang="en">
<head>
<meta charset="utf-8">
<title>6 Steps Hiring Process</title>
<link rel="stylesheet" href="https://fonts.googleapis.com/css2?family=Montserrat:wght@300;400;500;700;800&display=swap">
<style>
  :root {
    --frame: #4d4d4d;
    --card: #ffffff;
    --ink: #555555;
    --rule: #d2d2d2;
    --dot: #6f6f6f;
    --step-1: #3ccbe4;
    --step-2: #2389c4;
    --step-3: #5a84cc;
    --step-4: #937fbf;
    --step-5: #6a4aa8;
    --step-6: #6e3992;
    --col: 186.33px;
  }
  * { margin: 0; padding: 0; box-sizing: border-box; }
  html, body { width: 1200px; height: 733px; overflow: hidden; }
  body {
    background: var(--frame);
    font-family: "Montserrat", Arial, sans-serif;
    position: relative;
  }
  .card {
    position: absolute;
    left: 41px; top: 42px;
    width: 1118px; height: 649px;
    background: var(--card);
    border-radius: 20px;
    overflow: hidden;
  }
  .heading {
    position: absolute; top: 66px; left: 0; width: 100%;
    text-align: center;
    font-size: 29px; font-weight: 500; color: var(--ink);
    letter-spacing: 0.3px;
  }
  .subheading {
    position: absolute; top: 120px; left: 0; width: 100%;
    text-align: center;
    font-size: 20px; font-weight: 300; color: var(--ink);
    letter-spacing: 0.5px;
  }
  .rule {
    position: absolute; top: 171px; left: 44px; width: 1032px;
    height: 1px; background: var(--rule);
  }
  .timeline {
    position: absolute; top: 302px; left: 44px; width: 1035px; height: 4px;
    background-image: radial-gradient(circle, var(--dot) 1.3px, transparent 1.7px);
    background-size: 9.3px 4px;
  }
  .steps {
    position: absolute; inset: 0; display: flex;
    list-style: none;
  }
  .step {
    position: relative; display: block; list-style: none;
    width: var(--col); height: 100%; --c: var(--step-1);
  }
  .step:nth-child(2) { --c: var(--step-2); }
  .step:nth-child(3) { --c: var(--step-3); }
  .step:nth-child(4) { --c: var(--step-4); }
  .step:nth-child(5) { --c: var(--step-5); }
  .step:nth-child(6) { --c: var(--step-6); }
  .step-icon {
    position: absolute; top: 204px; left: 50%; margin-left: -41px;
    width: 82px; height: 82px;
  }
  .step-icon .ring { fill: #fff; stroke: var(--c); stroke-width: 2; }
  .step-icon .line { fill: none; stroke: var(--c); stroke-width: 2.5; stroke-linecap: round; stroke-linejoin: round; }
  .step-icon .solid { fill: var(--c); }
  .step-icon .paper { fill: #fff; stroke: var(--c); stroke-width: 2.5; stroke-linejoin: round; }
  .step-marker {
    position: absolute; top: 298px; left: 50%; margin-left: -6px;
    width: 12px; height: 12px; border-radius: 50%;
    border: 1.5px solid var(--c); background: var(--card);
    box-shadow: 0 0 0 7px var(--card);
  }
  .step-marker::after {
    content: ""; position: absolute; inset: 2px; border-radius: 50%; background: var(--c);
  }
  .step-stem {
    position: absolute; top: 317px; left: 50%; width: 1px; height: 16px;
    background: var(--ink);
  }
  .step-band { position: absolute; top: 355px; left: 0; width: 100%; height: 223px; }
  .step-band polygon { fill: var(--c); }
  .step-number {
    position: absolute; top: 336px; left: 0; width: 100%;
    text-align: center; font-size: 29px; font-weight: 700; color: var(--c);
  }
  .step-title {
    position: absolute; top: 426px; left: 0; width: 100%;
    text-align: center; color: #fff;
    font-size: 17px; font-weight: 800; line-height: 27.5px;
    letter-spacing: 0.6px; text-transform: uppercase;
  }
</style>
</head>
<body>
<main class="card">
  <h1 class="heading">6 Steps Infographic Design Project</h1>
  <p class="subheading">(Title)</p>
  <div class="rule"></div>
  <div class="timeline"></div>

  <ol class="steps">
    <li class="step">
      <svg class="step-icon" viewBox="0 0 82 82" role="img" aria-label="Phone and chat icon">
        <circle class="ring" cx="41" cy="41" r="39.5"/>
        <path class="solid" d="M13 24 Q8 41 13 58 L20 56 Q17 41 20 26 Z"/>
        <path class="solid" d="M69 24 Q74 41 69 58 L62 56 Q65 41 62 26 Z"/>
        <rect class="line" x="24" y="27" width="22" height="15" rx="3"/>
        <path class="line" d="M29 42 L27 48 L34 42"/>
        <rect class="paper" x="35" y="35" width="22" height="15" rx="3"/>
        <path class="paper" d="M52 50 L54 56 L47 50"/>
      </svg>
      <span class="step-marker"></span><span class="step-stem"></span>
      <svg class="step-band" viewBox="0 0 186.33 223" preserveAspectRatio="none"><polygon points="0,0 53,0 93.2,41 133,0 186.33,0 186.33,223 0,223"/></svg>
      <span class="step-number">01</span>
      <h2 class="step-title">Strong<br>Phone<br>Interview</h2>
    </li>
    <li class="step">
      <svg class="step-icon" viewBox="0 0 82 82" role="img" aria-label="Checklist clipboard and pen icon">
        <circle class="ring" cx="41" cy="41" r="39.5"/>
        <rect class="paper" x="24" y="20" width="30" height="42" rx="3"/>
        <rect class="solid" x="32" y="16" width="14" height="7" rx="2"/>
        <path class="line" d="M29 31 l2 2 l4 -4 M38 31 h11 M29 40 l2 2 l4 -4 M38 40 h11 M29 49 l2 2 l4 -4 M38 49 h11"/>
        <path class="solid" d="M60 24 L65 29 L52 50 L47 52 L48 46 Z"/>
      </svg>
      <span class="step-marker"></span><span class="step-stem"></span>
      <svg class="step-band" viewBox="0 0 186.33 223" preserveAspectRatio="none"><polygon points="0,0 53,0 93.2,41 133,0 186.33,0 186.33,223 0,223"/></svg>
      <span class="step-number">02</span>
      <h2 class="step-title">Pre-<br>Employment</h2>
    </li>
    <li class="step">
      <svg class="step-icon" viewBox="0 0 82 82" role="img" aria-label="Meeting desk icon">
        <circle class="ring" cx="41" cy="41" r="39.5"/>
        <rect class="solid" x="30" y="22" width="22" height="9" rx="3"/>
        <rect class="paper" x="19" y="34" width="44" height="22" rx="2"/>
        <path class="line" d="M24 56 v8 M58 56 v8"/>
        <rect class="solid" x="30" y="48" width="22" height="8" rx="3"/>
      </svg>
      <span class="step-marker"></span><span class="step-stem"></span>
      <svg class="step-band" viewBox="0 0 186.33 223" preserveAspectRatio="none"><polygon points="0,0 53,0 93.2,41 133,0 186.33,0 186.33,223 0,223"/></svg>
      <span class="step-number">03</span>
      <h2 class="step-title">Pre-Do In<br>Person<br>Interview</h2>
    </li>
    <li class="step">
      <svg class="step-icon" viewBox="0 0 82 82" role="img" aria-label="Speech bubble with ticks icon">
        <circle class="ring" cx="41" cy="41" r="39.5"/>
        <rect class="line" x="18" y="20" width="30" height="20" rx="3"/>
        <path class="line" d="M24 40 L22 47 L30 40"/>
        <path class="line" d="M24 30 l3 3 l5 -6 M35 30 l3 3 l5 -6"/>
        <rect class="solid" x="40" y="46" width="26" height="16" rx="3"/>
        <path class="solid" d="M58 62 L60 68 L52 62 Z"/>
      </svg>
      <span class="step-marker"></span><span class="step-stem"></span>
      <svg class="step-band" viewBox="0 0 186.33 223" preserveAspectRatio="none"><polygon points="0,0 53,0 93.2,41 133,0 186.33,0 186.33,223 0,223"/></svg>
      <span class="step-number">04</span>
      <h2 class="step-title">Second<br>Interview</h2>
    </li>
    <li class="step">
      <svg class="step-icon" viewBox="0 0 82 82" role="img" aria-label="Document with pencil icon">
        <circle class="ring" cx="41" cy="41" r="39.5"/>
        <rect class="paper" x="22" y="18" width="32" height="44" rx="3"/>
        <circle class="line" cx="38" cy="29" r="6"/>
        <path class="line" d="M29 42 h18 M29 48 h18 M29 54 h12"/>
        <path class="solid" d="M59 32 L64 37 L51 57 L46 59 L47 53 Z"/>
      </svg>
      <span class="step-marker"></span><span class="step-stem"></span>
      <svg class="step-band" viewBox="0 0 186.33 223" preserveAspectRatio="none"><polygon points="0,0 53,0 93.2,41 133,0 186.33,0 186.33,223 0,223"/></svg>
      <span class="step-number">05</span>
      <h2 class="step-title">Reference<br>Checks</h2>
    </li>
    <li class="step">
      <svg class="step-icon" viewBox="0 0 82 82" role="img" aria-label="Pinned offer card with tick icon">
        <circle class="ring" cx="41" cy="41" r="39.5"/>
        <rect class="paper" x="22" y="22" width="38" height="34" rx="3" transform="rotate(-6 41 39)"/>
        <circle class="solid" cx="41" cy="20" r="4"/>
        <path class="line" d="M31 40 l7 7 l13 -14"/>
        <path class="line" d="M27 62 h28"/>
      </svg>
      <span class="step-marker"></span><span class="step-stem"></span>
      <svg class="step-band" viewBox="0 0 186.33 223" preserveAspectRatio="none"><polygon points="0,0 53,0 93.2,41 133,0 186.33,0 186.33,223 0,223"/></svg>
      <span class="step-number">06</span>
      <h2 class="step-title">Job<br>Offer</h2>
    </li>
  </ol>
</main>
</body>
</html>
```